Scrum Master & Agile IT Coach Needing Business Website

Hello, my name is Brent Ellison
I am a project manger, scrum master, & agile coach. I work with IT development teams on major projects for Fortune 500 companies . My project management business has a website and can be found here: www.tq-steadfast.example

I have launched a new company, ALL focused on IT Agile Coaching, I am looking to have a website created for my new company - the name of the new company is: Pins and Pegs - Agile IT Coaching and Training.
I have a logo and it is provided in the materials. I like to logo; I am open to different color pallets.

The website will have a total of 7 pages; I have content for 5 of the 7 pages prepared; the other 2 pages will say under construction.

Page 1 Who am I, What I do, My Experience
Demonstrated experience and progression from Scrum Master to
Program Manager to Coach

Page 2 Pins & Pegs - Agile Team Coaching
teams working major IT projects, multiple months/years

Page 3 Coaching @ the Team Level

Page 4 Coaching @ the Program Level ; ScaleWay ART level

Pages 5 -6 Under Construction

Page 7 Presentations, Slide Decks, Reference Materials

Mentors Nook need to have this highlighted somewhere Monthly Blog
Updates

Industry/Entity Type

IT development

Coding

Coded - Design and coding required

Number of Pages Required

5+ page

Requirements
Must have
• the website must be bold - I want those who visit to remember coming to my coaching site
Nice to have
• nice to have will be a modern / futuristic website; I work with IT developers, I want a website they will like
Should not have
• should not be stiff - it should be professional but fun

```html
<!DOCTYPE html>
<html lang="en">
<head>
<meta charset="utf-8">
<title>Pins &amp; Pegs - Agile IT Coaching and Training</title>
<link rel="stylesheet" href="https://fonts.googleapis.com/css2?family=Oswald:wght@300;400;500&family=Montserrat:wght@400;600&display=swap">
<style>
:root{
  --navy:#0a3778;
  --navy-deep:#062a61;
  --hero-a:#0c4ea6;
  --hero-b:#06306e;
  --sky:#1aa3e8;
  --ink:#1d2b4a;
  --grey:#e9eaec;
  --white:#ffffff;
}
*{margin:0;padding:0;box-sizing:border-box}
html,body{width:1200px;height:3140px;overflow:hidden;background:var(--white)}
body{position:relative;font-family:"Oswald",sans-serif;color:var(--ink)}
.abs{position:absolute}
.brand{display:flex;align-items:center;gap:8px;font-family:"Oswald",sans-serif;font-weight:500;font-size:24px;color:var(--navy)}
.brand-mark{width:18px;height:18px;border:2px solid var(--navy)}
.nav{font-size:10px;text-transform:uppercase;color:var(--navy);top:52px;height:22px}
.nav a{color:var(--navy);text-decoration:none;position:absolute;white-space:nowrap;top:5px}
.nav .current{color:var(--sky)}
.btn{display:flex;align-items:center;justify-content:center;font-size:9px;letter-spacing:.3px;text-transform:uppercase;color:var(--white);background:var(--sky);border-radius:2px}
.btn-navy{background:var(--navy)}
.btn-ghost{background:var(--white);color:var(--navy)}
.hero{left:150px;top:86px;width:900px;height:424px;background:radial-gradient(ellipse at 60% 40%,var(--hero-a),var(--hero-b) 75%);overflow:hidden}
.hero-photo{left:477px;top:27px;width:256px;height:372px;border-radius:110px 110px 0 0;background:linear-gradient(160deg,#6d90c4,#3d5f95 60%,#2b4675)}
.hero h1{position:absolute;z-index:2;left:150px;top:108px;width:340px;font-weight:300;font-size:27px;line-height:34px;color:var(--white)}
.intro{left:150px;width:900px;text-align:center}
.intro h2{font-weight:400;font-size:23px;color:var(--sky)}
.intro h3{font-weight:300;font-size:23px;color:var(--navy);margin-top:2px}
.intro .lead{font-size:9px;color:var(--navy);margin-top:12px}
.intro .body{font-family:"Montserrat",sans-serif;font-size:7px;line-height:11.5px;color:#555;width:580px;margin:12px auto 0}
.list-title{font-weight:300;font-size:16px;color:var(--sky)}
.ticks{list-style:none;margin-top:12px}
.ticks li{position:relative;padding-left:16px;font-size:9.5px;color:var(--white);line-height:12px;margin-bottom:10px}
.ticks li::before{content:"";position:absolute;left:0;top:2px;width:7px;height:4px;border-left:1.5px solid var(--sky);border-bottom:1.5px solid var(--sky);transform:rotate(-45deg)}
.section-title{left:150px;width:900px;text-align:center;font-weight:400;font-size:23px;color:var(--navy)}
.exp-card{border:1.5px solid var(--sky);border-top-width:2px;background:var(--white);padding:22px 16px 0 18px;width:186px;height:276px}
.exp-card h4{font-weight:400;font-size:11.5px;line-height:14px;color:var(--sky);margin-bottom:12px}
.exp-card .ticks li{color:var(--ink);font-size:8.5px;line-height:11px;margin-bottom:11px;font-weight:300}
.post{background:var(--white);width:164px;height:184px;box-shadow:0 4px 12px rgba(0,0,0,.08);text-align:center}
.post .thumb{height:92px;background:linear-gradient(135deg,#b9c7d8,#6e7f95)}
.post .date{font-size:8px;color:var(--sky);margin-top:20px}
.post .excerpt{font-size:8.5px;line-height:11px;color:var(--navy);font-weight:300;margin-top:8px}
.post .more{font-size:7.5px;color:var(--navy);margin-top:6px;font-weight:500}
.footer-title{font-weight:300;font-size:14px;color:var(--navy)}
.contact-line{font-family:"Montserrat",sans-serif;font-size:7px;color:var(--navy);display:flex;gap:8px;align-items:flex-start}
.quick{list-style:none;font-family:"Montserrat",sans-serif;font-size:7px;color:var(--navy)}
.quick li{height:14px}
.social{width:22px;height:22px;background:var(--navy);left:877px}
.social.alt{background:var(--sky)}
.copy{font-family:"Montserrat",sans-serif;font-size:6.5px;color:var(--navy)}
</style>
</head>
<body>

<!-- Header -->
<div class="abs brand" style="left:302px;top:50px"><span class="brand-mark"></span>Pins &amp; Pegs</div>
<nav class="abs nav" style="left:0;width:1200px">
  <a class="current" style="left:532px">Home</a>
  <a style="left:578px">About Us</a>
  <a style="left:636px">Coaching</a>
  <a style="left:694px">Blog</a>
  <a style="left:737px;font-size:11px;top:3px;font-weight:500">
    <svg width="9" height="9" viewBox="0 0 10 10" style="vertical-align:-1px;margin-right:4px"><path d="M2 1l2 2-1 1.5c.6 1.2 1.3 1.9 2.5 2.5L7 6l2 2-1.2 1.5C4.5 9.5.5 5.5.5 2.2z" fill="#1aa3e8"/></svg>(555) 014-2290</a>
</nav>
<div class="abs btn btn-navy" style="left:834px;top:52px;width:65px;height:22px">Contact Us</div>

<!-- Hero -->
<section class="abs hero">
  <div class="abs hero-photo" role="img" aria-label="Portrait of Brent Ellison in a blue checked suit"></div>
  <h1>Demonstrate Experience and Progression from Scrum Master to Program Manager to Coach</h1>
  <div class="abs btn" style="left:150px;top:222px;width:66px;height:22px;z-index:2">Contact Us</div>
  <svg class="abs" style="left:0;top:0;z-index:3" width="900" height="424" viewBox="0 0 900 424">
    <path d="M0 310 Q450 450 900 310 L900 424 L0 424Z" fill="#ffffff"/>
    <path d="M60 350 Q450 470 880 345" fill="none" stroke="#1aa3e8" stroke-width="5"/>
  </svg>
</section>

<!-- Intro -->
<section class="abs intro" style="top:550px">
  <h2>Brent Ellison</h2>
  <h3>Senior Scrum Master &amp; Team Agile Coach</h3>
  <p class="lead">Brent Ellison is the Owner of Steadfast Delivery Group, LLC and serves as Principal Lead Consultant on waterfall and agile contract opportunities.</p>
  <p class="body">Brent brings 13+ years of experience to his clients - experience which encompasses various project management methodologies ranging from waterfall, agile, and mixed hybrid frameworks. A separating factor in the consultancy services provided at Steadfast Delivery Group, LLC is that Brent has spent years on both the Business and IT/IS sides of the project management business ...</p>
</section>
<div class="abs btn" style="left:568px;top:706px;width:64px;height:22px">Discover More</div>

<!-- Designations & Roles -->
<svg class="abs" style="left:150px;top:760px" width="900" height="506" viewBox="0 0 900 506">
  <path d="M0 19 Q450 97 900 19 L900 368 Q450 296 0 368Z" fill="#0a3778"/>
  <path d="M0 12 Q450 88 900 12" fill="none" stroke="#1aa3e8" stroke-width="5"/>
  <path d="M0 368 Q450 296 900 368 L900 506 L0 506Z" fill="#e9eaec"/>
  <path d="M0 362 Q450 288 900 362" fill="none" stroke="#1aa3e8" stroke-width="6"/>
  <rect x="357" y="9" width="186" height="262" fill="#ffffff" stroke="#1aa3e8" stroke-width="1.5"/>
</svg>
<div class="abs" role="img" aria-label="Business team shaking hands around a meeting table" style="left:517px;top:779px;width:166px;height:242px;background:linear-gradient(150deg,#e8edf3,#aab6c6 55%,#6a7b93)"></div>

<div class="abs" style="left:300px;top:862px;width:190px">
  <div class="list-title">Coaching Designations</div>
  <ul class="ticks">
    <li>CAP-SP</li><li>Certified Agile Foundations Educator</li><li>ATP-TC</li><li>ScaleWay Advanced Team Lead</li><li>A-CAP</li>
  </ul>
</div>
<div class="abs btn" style="left:300px;top:1010px;width:66px;height:22px">Contact Us</div>

<div class="abs" style="left:712px;top:862px;width:180px">
  <div class="list-title">Roles I Have Held</div>
  <ul class="ticks">
    <li>Sr. Scrum Master</li><li>Advanced ScaleWay Team Lead</li><li>Hybrid Scrum Master/ Project Manager</li><li>Business (Finance Transformation Program Manager</li>
  </ul>
</div>
<div class="abs btn btn-ghost" style="left:712px;top:1010px;width:66px;height:22px">Contact Us</div>

<!-- Certification badges -->
<svg class="abs" style="left:300px;top:1130px" width="600" height="100" viewBox="0 0 600 100" role="img" aria-label="Certification badges">
  <circle cx="60" cy="50" r="46" fill="#1aa3e8"/>
  <polygon points="183,4 224,27 224,73 183,96 142,73 142,27" fill="#ffffff" stroke="#1d2b4a" stroke-width="5"/>
  <circle cx="312" cy="50" r="46" fill="#f4b43a"/>
  <polygon points="435,4 481,50 435,96 389,50" fill="#1d3a63"/>
  <circle cx="552" cy="50" r="42" fill="#f39c46"/>
</svg>

<!-- Experience -->
<h2 class="abs section-title" style="top:1308px">What is My Experience</h2>
<div class="abs exp-card" style="left:300px;top:1354px">
  <h4>As a ScaleWay Adv Team Lead, I:</h4>
  <ul class="ticks">
    <li>Stand up teams</li><li>Run development efforts concurrently leading multiple teams</li><li>Run ScaleWay ceremonies</li><li>Scrum of Scrums facilitator</li><li>Increment Planning team facilitator (multiple teams on ART)</li><li>Teach and coach to advanced development team strategies</li><li>Lead program level communications and business status updates on behalf of the team</li>
  </ul>
</div>
<div class="abs exp-card" style="left:507px;top:1354px">
  <h4>As a Hybrid Scrum Master / Project Manager, I:</h4>
  <ul class="ticks">
    <li>Standup teams</li><li>Run multiple program level projects simultaneously</li><li>Implement custom hybrid development strategies</li><li>Manage to project triple constraints</li><li>Communications lead and business liaison</li><li>Use multiple coaching styles based on team and project</li>
  </ul>
</div>
<div class="abs exp-card" style="left:713px;top:1354px">
  <h4>Business Transformation Program Manager</h4>
  <ul class="ticks">
    <li>Lead business transformation efforts at the program level</li><li>Work with multiple product owners, business analysts, and business stake holders on requirements</li><li>Lead the international rollout, onboarding, and support of new transformational CRM tool, CloudDesk</li><li>Standup and lead multi-functional teams consisting of business and technology team members</li><li>Serve as program organization and communications lead</li>
  </ul>
</div>

<!-- Coaching band -->
<svg class="abs" style="left:150px;top:1660px" width="900" height="290" viewBox="0 0 900 290">
  <path d="M0 8 Q450 62 900 8 L900 272 Q450 188 0 272Z" fill="#0a3778"/>
  <path d="M0 14 Q450 70 900 14" fill="none" stroke="#1aa3e8" stroke-width="5"/>
</svg>
<h2 class="abs section-title" style="top:1756px;color:#fff">Where Does Coaching Come in to Play</h2>
<article class="abs post" style="left:340px;top:1804px">
  <div class="thumb" role="img" aria-label="Colleagues reviewing documents at a desk"></div>
  <div class="date">JAN. 18, 2022</div>
  <p class="excerpt">Lorem Ipsum is simply dummy text<br>printing typesetting ...</p>
  <div class="more">Read More</div>
</article>
<article class="abs post" style="left:519px;top:1804px">
  <div class="thumb" role="img" aria-label="Hands working over charts and a laptop" style="background:linear-gradient(135deg,#7f9bb8,#3f5572)"></div>
  <div class="date">JAN. 18, 2022</div>
  <p class="excerpt">Lorem Ipsum is simply dummy text<br>printing typesetting ...</p>
  <div class="more">Read More</div>
</article>
<article class="abs post" style="left:696px;top:1804px">
  <div class="thumb" role="img" aria-label="Team meeting in a bright conference room" style="background:linear-gradient(135deg,#d0d6de,#8a94a2)"></div>
  <div class="date">JAN. 18, 2022</div>
  <p class="excerpt">Lorem Ipsum is simply dummy text<br>printing typesetting ...</p>
  <div class="more">Read More</div>
</article>
<div class="abs btn btn-navy" style="left:568px;top:2009px;width:64px;height:22px">View All</div>

<!-- Footer -->
<footer class="abs" style="left:150px;top:2048px;width:900px;height:276px;background:var(--grey)">
  <svg class="abs" style="left:0;top:0" width="900" height="50" viewBox="0 0 900 50">
    <path d="M0 0 L900 0 L900 4 Q450 68 0 4Z" fill="#ffffff"/>
    <path d="M0 4 Q450 68 900 4" fill="none" stroke="#1aa3e8" stroke-width="5"/>
  </svg>
</footer>
<div class="abs brand" style="left:302px;top:2138px"><span class="brand-mark"></span>Pins &amp; Pegs</div>

<div class="abs footer-title" style="left:512px;top:2132px">Contact Us</div>
<div class="abs contact-line" style="left:512px;top:2165px;font-family:'Oswald',sans-serif;font-size:11px;font-weight:300">
  <svg width="9" height="9" viewBox="0 0 10 10"><path d="M2 1l2 2-1 1.5c.6 1.2 1.3 1.9 2.5 2.5L7 6l2 2-1.2 1.5C4.5 9.5.5 5.5.5 2.2z" fill="#1aa3e8"/></svg>555-014-7890</div>
<div class="abs contact-line" style="left:512px;top:2191px">
  <svg width="8" height="7" viewBox="0 0 8 7"><rect x=".5" y=".5" width="7" height="6" fill="#1aa3e8"/></svg>brent.ellison@tq-steadfast.example</div>
<div class="abs contact-line" style="left:512px;top:2214px;line-height:11px">
  <svg width="7" height="9" viewBox="0 0 7 9"><path d="M3.5 0A3.5 3.5 0 0 0 0 3.5C0 6 3.5 9 3.5 9S7 6 7 3.5A3.5 3.5 0 0 0 3.5 0z" fill="#1aa3e8"/></svg><span>14 Harbor Lane, Lakeview, IA,<br>50210 United States</span></div>

<div class="abs footer-title" style="left:736px;top:2132px">Quick Links</div>
<ul class="abs quick" style="left:736px;top:2164px">
  <li>Home</li><li>About Us</li><li>Coaching</li><li>Blog</li><li>Contact Us</li>
</ul>

<div class="abs social" style="top:2137px"></div>
<div class="abs social alt" style="top:2166px"></div>
<div class="abs social" style="top:2194px"></div>

<div class="abs copy" style="left:300px;top:2280px">© 2022 <b>Pins and Pegs</b>. All Right Reserved</div>
<svg class="abs" style="left:968px;top:2274px" width="12" height="14" viewBox="0 0 12 14"><path d="M6 0L12 14 6 10 0 14Z" fill="#1aa3e8"/></svg>

</body>
</html>
```